Monthly Report PowerPoint Template

We are looking for a set of slides to use as a template for a report that we send out monthly on the state of the solar and storage market. It should be professional and low profile, attached are the slides we currently use/would like to replace: 1) title slide, 2) content summary, 3) content, and 4) section break. We are mainly concerned about a new design for 2), we are using the basic PowerPoint table and would like both a new table style and a version that is more visual. Thanks!

Requirements
Must have
• Light theme
Should not have
• No stock images

```html
<!DOCTYPE html>
<html lang="en">
<head>
<meta charset="utf-8">
<title>Volta Insight — Monthly Report Template</title>
<link rel="stylesheet" href="https://fonts.googleapis.com/css2?family=Poppins:wght@300;400;500;600;700;800&display=swap">
<style>
:root{
  --navy:#1d4a7a;
  --navy-dark:#163b63;
  --gold:#f2b84b;
  --sky:#a9d4e0;
  --ink:#222;
  --muted:#7a7a7a;
  --card:#eef0f2;
  --board:#d7d9dc;
}
*{box-sizing:border-box;margin:0;padding:0}
html,body{width:1045px;height:1200px;overflow:hidden;background:var(--board);font-family:'Poppins',sans-serif}
.board{position:relative;width:1045px;height:1200px}
.slide{position:absolute;width:525px;height:295px;background:#fff;transform:scale(.5831);transform-origin:0 0;overflow:hidden;box-shadow:0 3px 10px rgba(0,0,0,.22)}
.abs{position:absolute}
.eyebrow{color:var(--gold);font-weight:500;line-height:1.05;text-transform:uppercase}
.heading{color:var(--navy);font-weight:700;line-height:1.05;text-transform:uppercase}
.copy{font-size:6.6px;color:var(--muted);line-height:1.5}
.sub{font-size:10px;font-weight:600;color:var(--ink)}
.photo{position:absolute}
.brand{font-weight:500;color:var(--navy);letter-spacing:.2px}
.footer-brand{position:absolute;left:12px;top:262px;display:flex;align-items:center;gap:3px;font-size:5px;font-weight:500;color:var(--navy)}
.footer-brand i{display:block;width:12px;height:12px;border-radius:50%;border:2px solid var(--gold);background:#fff}
.footer-rule{position:absolute;left:50px;right:22px;top:277px;height:1px;background:var(--navy)}
.page-no{position:absolute;right:16px;top:278px;font-size:6px;color:var(--ink)}
.chart{position:absolute;left:0;top:0}
.chart text{font-family:'Poppins',sans-serif}
.toc-row{position:absolute;left:270px;width:200px;height:12px;font-size:6.5px;color:var(--navy);font-weight:500}
.toc-row:before{content:"";position:absolute;left:0;top:3px;width:4px;height:4px;border-radius:50%;background:var(--gold)}
.toc-row span{position:absolute;left:10px;top:0}
.toc-row b{position:absolute;left:0;right:14px;top:11px;height:1px;background:#f3d9a0}
.toc-row em{position:absolute;right:0;top:5px;width:13px;height:13px;border-radius:50%;background:var(--navy);color:#fff;font-style:normal;font-size:5.5px;font-weight:600;text-align:center;line-height:13px}
.tile{position:absolute;width:84px;height:80px;padding:10px;color:#fff}
.tile h4{font-size:6px;font-weight:700;margin:8px 0 4px}
.tile p{font-size:4.6px;line-height:1.5;opacity:.9}
.tile svg{display:block}
.client{position:absolute;width:88px;height:48px;border:2px solid var(--navy);border-radius:9px;display:flex;align-items:center;justify-content:center;font-size:10px;font-weight:600;color:var(--navy)}
.check{position:absolute;display:flex;align-items:center;gap:6px;font-size:11px;font-weight:600;color:var(--navy)}
.check i{display:block;width:13px;height:13px;border-radius:3px;background:var(--gold);position:relative}
.check i:after{content:"";position:absolute;left:4px;top:2px;width:3px;height:6px;border:solid #fff;border-width:0 1.5px 1.5px 0;transform:rotate(45deg)}
.data-table{position:absolute;left:184px;top:77px;width:316px;border-collapse:collapse;border:1.5px solid #888;font-size:5.2px}
.data-table th{height:18px;font-weight:600;color:var(--navy);background:var(--gold);border:1px solid #fff}
.data-table th:first-child{background:var(--navy);color:#fff}
.data-table td{height:21px;border:1px solid #9a9a9a;padding-left:6px;color:var(--navy);font-weight:500}
.data-table tr:nth-child(even) td{background:#f1f1f1}
</style>
</head>
<body>
<main class="board">

<!-- 1 Title -->
<section class="slide" style="left:48px;top:43.8px">
  <div class="abs brand" style="left:32px;top:24px;font-size:19px">Volta Insight</div>
  <div class="photo" role="img" aria-label="Solar panels in a grassy field under a sunset sky" style="left:216px;top:33px;width:309px;height:229px;background:linear-gradient(160deg,#c9c2a6 0%,#6e7566 45%,#2c3a34 75%,#4b5a2f 100%)"></div>
  <div class="abs" style="left:0;top:82px;width:297px;height:146px;background:var(--navy);border-radius:0 14px 14px 0"></div>
  <div class="abs" style="left:34px;top:108px;font-size:34px;font-weight:800;color:var(--gold);line-height:1">BUSINESS</div>
  <div class="abs" style="left:34px;top:148px;font-size:11px;font-weight:600;color:#fff">Presentation Template</div>
  <div class="abs" style="left:34px;top:168px;font-size:6.4px;color:#fff;line-height:1.5">Lorem ipsum is simply dummy text<br>of the printing and typesetting industry.</div>
  <div class="abs" style="left:32px;top:244px;display:flex;align-items:center;gap:6px;font-size:8px;color:#555"><i style="display:block;width:13px;height:13px;border-radius:50%;background:var(--navy)"></i>Your Website Name Goes Here</div>
</section>

<!-- 2 Table of content -->
<section class="slide" style="left:372.6px;top:43.8px">
  <div class="abs eyebrow" style="left:55px;top:104px;font-size:15px;font-weight:400">Table of</div>
  <div class="abs heading" style="left:55px;top:121px;font-size:26px">Content</div>
  <p class="abs copy" style="left:55px;top:157px;width:175px;font-size:6.3px;color:#555">Lorem Ipsum is simply dummy text of the printing and typesetting industry. Lorem Ipsum has been the industry's standard dummy text ever since the 1500s.</p>
  <div class="toc-row" style="top:64px"><span>Simple Text One</span><b></b><em>02</em></div>
  <div class="toc-row" style="top:93px"><span>Simple Text Two</span><b></b><em>04</em></div>
  <div class="toc-row" style="top:122px"><span>Simple Text Three</span><b></b><em>06</em></div>
  <div class="toc-row" style="top:151px"><span>Simple Text Four</span><b></b><em>08</em></div>
  <div class="toc-row" style="top:180px"><span>Simple Text Five</span><b></b><em>10</em></div>
  <div class="toc-row" style="top:209px"><span>Simple Text Six</span><b></b><em>12</em></div>
  <div class="footer-brand"><i></i>Volta Insight</div><div class="footer-rule"></div><div class="page-no">2</div>
</section>

<!-- 3 Products and services -->
<section class="slide" style="left:694.5px;top:43.8px">
  <div class="abs eyebrow" style="left:23px;top:28px;font-size:16px;font-weight:600">Products</div>
  <div class="abs heading" style="left:23px;top:46px;font-size:21px">And Services</div>
  <svg class="chart" width="525" height="295">
    <g fill="none" stroke="var(--gold)" stroke-width="2">
      <path d="M52 120a9 9 0 0 1 17-5 7 7 0 0 1 6 12H53a6 6 0 0 1-1-7z"/><path d="M62 113l-4 8h6l-4 8"/>
      <circle cx="62" cy="163" r="7"/><circle cx="62" cy="163" r="3"/>
      <rect x="52" y="207" width="20" height="15" rx="2"/><path d="M57 219v-5M62 219v-8M67 219v-3"/>
    </g>
  </svg>
  <div class="abs sub" style="left:85px;top:92px">Lorem ipsum dolor.</div>
  <p class="abs copy" style="left:85px;top:106px;width:145px">Lorem ipsumectetuer adipiscing elit, sed diam nonummy nibh euismod tincidunt</p>
  <div class="abs sub" style="left:85px;top:146px">Lorem ipsum dolor.</div>
  <p class="abs copy" style="left:85px;top:160px;width:145px">Lorem ipsumectetuer adipiscing elit, sed diam nonummy nibh euismod tincidunt</p>
  <div class="abs sub" style="left:85px;top:200px">Lorem ipsum dolor.</div>
  <p class="abs copy" style="left:85px;top:214px;width:145px">Lorem ipsumectetuer adipiscing elit, sed diam nonummy nibh euismod tincidunt</p>
  <div class="photo" role="img" aria-label="Technician kneeling beside solar panels with a test case" style="left:273px;top:40px;width:209px;height:218px;border-radius:20px;background:linear-gradient(170deg,#6f8aa6 0%,#9aa7ae 40%,#857c6c 75%,#b7a98e 100%)"></div>
  <div class="footer-brand"><i></i>Volta Insight</div><div class="footer-rule"></div><div class="page-no">2</div>
</section>

<!-- 4 About our company -->
<section class="slide" style="left:48px;top:229.9px">
  <svg class="chart" width="525" height="295">
    <polygon points="250,0 272,0 345,158 322,140" fill="var(--gold)"/>
    <polygon points="272,0 525,0 525,158 345,158" fill="#5f7486" role="img" aria-label="Engineers inspecting rooftop solar panels"/>
  </svg>
  <div class="abs" style="left:38px;top:37px;font-size:6.5px;font-weight:500;color:var(--ink)">A BUSINESS TEXT HERE</div>
  <div class="abs eyebrow" style="left:38px;top:48px;font-size:24px;font-weight:700">About Our</div>
  <div class="abs heading" style="left:38px;top:74px;font-size:24px">Company</div>
  <p class="abs copy" style="left:38px;top:103px;width:200px;color:#444">Lorem ipsum dolor amet consectetur adipisc eiusmod incididunt labore dolore magna ullamco aliqua. Aliquip commodo consequat.</p>
  <svg class="chart" width="525" height="295">
    <g fill="var(--gold)"><circle cx="46" cy="168" r="6"/><circle cx="46" cy="197" r="6"/><circle cx="46" cy="226" r="6"/><circle cx="263" cy="180" r="8"/><circle cx="388" cy="180" r="8"/></g>
    <g fill="none" stroke="#fff" stroke-width="1.4"><path d="M43 168l2 2 4-4M43 197l2 2 4-4M43 226l2 2 4-4"/><circle cx="263" cy="180" r="3"/><path d="M384 183c1-4 4-5 7-5M388 175l3 3-3 3"/></g>
  </svg>
  <p class="abs copy" style="left:62px;top:160px;width:150px;font-size:5.6px;color:#444">Lorem Ipsum is simply dummy text ofn the print and typeseting magna aliqua.</p>
  <p class="abs copy" style="left:62px;top:189px;width:150px;font-size:5.6px;color:#444">Lorem Ipsum is simply dummy text ofn the print and typeseting magna aliqua.</p>
  <p class="abs copy" style="left:62px;top:218px;width:150px;font-size:5.6px;color:#444">Lorem Ipsum is simply dummy text ofn the print and typeseting magna aliqua.</p>
  <div class="abs" style="left:276px;top:176px;font-size:7.5px;font-weight:600;color:var(--navy)">Write Simple Text</div>
  <p class="abs copy" style="left:256px;top:198px;width:115px;font-size:5.2px;color:#444">Lorem ipsum is simply dummy text a print and typeset industry has text ever since the 1500s.</p>
  <div class="abs" style="left:401px;top:176px;font-size:7.5px;font-weight:600;color:var(--navy)">Write Simple Text</div>
  <p class="abs copy" style="left:386px;top:198px;width:115px;font-size:5.2px;color:#444">Lorem ipsum is simply dummy text a print and typeset industry has text ever since the 1500s.</p>
  <div class="footer-brand"><i></i>Volta Insight</div><div class="footer-rule"></div><div class="page-no">3</div>
</section>

<!-- 5 Section break -->
<section class="slide" style="left:372.6px;top:229.9px">
  <div class="photo" role="img" aria-label="Blue-tinted solar field backdrop" style="left:0;top:30px;width:525px;height:235px;background:linear-gradient(180deg,#2a5a8c 0%,var(--navy) 60%,#1a4270 100%)"></div>
  <div class="abs" style="left:145px;top:104px;font-size:42px;font-weight:800;color:var(--gold);line-height:1">01.</div>
  <div class="abs" style="left:252px;top:110px;font-size:20px;font-weight:700;color:var(--gold)">Part One.</div>
  <p class="abs" style="left:252px;top:138px;width:180px;font-size:7.2px;color:#dce6f0;line-height:1.45">Lorem ipsumectetuer adipiscing elit sed diam nonummy nibh euismod tincidunt</p>
  <div class="abs" style="left:418px;top:238px;font-size:12px;font-weight:500;color:#fff">Volta Insight</div>
</section>

<!-- 6 Mission & vision -->
<section class="slide" style="left:694.5px;top:229.9px">
  <div class="abs eyebrow" style="left:38px;top:18px;font-size:15px;font-weight:600">Company</div>
  <div class="abs heading" style="left:38px;top:34px;font-size:19px">Mission &amp; Vision</div>
  <p class="abs copy" style="left:38px;top:60px;width:195px">Lorem ipsum dolor sit amet, cons ectetuer adipiscing elit, sed diam nonummy nibh euismod tincidunt.Lorem ipsum dolor sit amet.</p>
  <div class="photo" role="img" aria-label="Wind turbines and solar panels at sunset" style="left:38px;top:122px;width:199px;height:114px;border-radius:12px;background:linear-gradient(180deg,#7e96aa 0%,#e7b466 50%,#3a4a5c 100%)"></div>
  <div class="abs" style="left:255px;top:68px;width:233px;height:76px;background:var(--card);border-radius:12px"></div>
  <div class="abs" style="left:255px;top:68px;width:56px;height:76px;background:var(--gold);border-radius:12px"></div>
  <div class="abs" style="left:255px;top:160px;width:233px;height:76px;background:var(--card);border-radius:12px"></div>
  <div class="abs" style="left:255px;top:160px;width:56px;height:76px;background:var(--navy);border-radius:12px"></div>
  <svg class="chart" width="525" height="295" fill="none" stroke="#fff" stroke-width="1.5">
    <path d="M275 114l8-8 6 6-8 8zM289 100l3 3M286 97l2-3M292 103l3-1"/>
    <path d="M274 208l14-14M274 194l14 14M272 196l4-4M286 210l4-4"/>
  </svg>
  <div class="abs" style="left:333px;top:78px;font-size:11px;font-weight:600;color:var(--ink)">Mission</div>
  <p class="abs copy" style="left:333px;top:94px;width:145px;font-size:6px">Lorem ipsum dolor sit amet, cons ectetuer adipiscing elit, sed diam nonummy nibh euismod tincidunt.</p>
  <div class="abs" style="left:333px;top:170px;font-size:11px;font-weight:600;color:var(--ink)">Vision</div>
  <p class="abs copy" style="left:333px;top:186px;width:145px;font-size:6px">Lorem ipsum dolor sit amet, cons ectetuer adipiscing elit, sed diam nonummy nibh euismod tincidunt.</p>
  <div class="footer-brand"><i></i>Volta Insight</div><div class="footer-rule"></div><div class="page-no">5</div>
</section>

<!-- 7 Summary report -->
<section class="slide" style="left:48px;top:418.9px">
  <div class="abs eyebrow" style="left:22px;top:14px;font-size:13px">Our Company</div>
  <div class="abs heading" style="left:22px;top:29px;font-size:18px">Summary Report</div>
  <svg class="chart" width="525" height="295" font-size="5">
    <text x="148" y="84" font-size="9" fill="#444">Chart Title</text>
    <g font-size="4.5" fill="#555"><rect x="128" y="90" width="3" height="3" fill="var(--navy)"/><text x="133" y="93">Series 3</text><rect x="157" y="90" width="3" height="3" fill="var(--gold)"/><text x="162" y="93">Series 2</text><rect x="186" y="90" width="3" height="3" fill="var(--sky)"/><text x="191" y="93">Series 1</text></g>
    <g fill="#555">
      <text x="42" y="122">Category 4</text><text x="42" y="155">Category 3</text><text x="42" y="188">Category 2</text><text x="42" y="222">Category 1</text>
    </g>
    <line x1="78" y1="106" x2="78" y2="234" stroke="#ccc" stroke-width=".6"/>
    <g>
      <rect x="78" y="112" width="190" height="5" fill="var(--navy)"/><rect x="78" y="119.5" width="106" height="5" fill="var(--gold)"/><rect x="78" y="127" width="171" height="5" fill="var(--sky)"/>
      <rect x="78" y="145" width="114" height="5" fill="var(--navy)"/><rect x="78" y="152.5" width="68" height="5" fill="var(--gold)"/><rect x="78" y="160" width="133" height="5" fill="var(--sky)"/>
      <rect x="78" y="178" width="76" height="5" fill="var(--navy)"/><rect x="78" y="185.5" width="167" height="5" fill="var(--gold)"/><rect x="78" y="193" width="95" height="5" fill="var(--sky)"/>
      <rect x="78" y="212" width="76" height="5" fill="var(--navy)"/><rect x="78" y="219.5" width="91" height="5" fill="var(--gold)"/><rect x="78" y="227" width="163" height="5" fill="var(--sky)"/>
    </g>
    <g fill="#444" font-size="4.5">
      <text x="271" y="117">5</text><text x="187" y="124">2.8</text><text x="252" y="132">4.5</text>
      <text x="195" y="150">3</text><text x="149" y="157">1.8</text><text x="214" y="165">3.5</text>
      <text x="157" y="183">2</text><text x="248" y="190">4.4</text><text x="176" y="198">2.5</text>
      <text x="157" y="217">2</text><text x="172" y="224">2.4</text><text x="244" y="232">4.3</text>
    </g>
    <text x="363" y="84" font-size="7" font-weight="600" fill="#444">SALES</text>
    <g font-size="4.5" fill="#555"><rect x="335" y="90" width="3" height="3" fill="var(--navy)"/><text x="340" y="93">1st Qtr</text><rect x="361" y="90" width="3" height="3" fill="var(--gold)"/><text x="366" y="93">2nd Qtr</text><rect x="389" y="90" width="3" height="3" fill="var(--sky)"/><text x="394" y="93">3rd Qtr</text></g>
    <g transform="rotate(-90 377 182)" fill="none" stroke-width="26">
      <circle cx="377" cy="182" r="50" stroke="var(--navy)" stroke-dasharray="201.06 314.16"/>
      <circle cx="377" cy="182" r="50" stroke="var(--gold)" stroke-dasharray="0 201.06 78.54 314.16"/>
      <circle cx="377" cy="182" r="50" stroke="var(--sky)" stroke-dasharray="0 279.6 34.56 314.16"/>
    </g>
    <g font-size="5" fill="#fff" font-weight="600"><text x="415" y="206">64%</text><text x="331" y="180">25%</text><text x="357" y="138">11%</text></g>
  </svg>
  <div class="footer-brand"><i></i>Volta Insight</div><div class="footer-rule"></div><div class="page-no">6</div>
</section>

<!-- 8 Report analytics -->
<section class="slide" style="left:372.6px;top:418.9px">
  <div class="abs eyebrow" style="left:35px;top:38px;font-size:13px">Our Company</div>
  <div class="abs heading" style="left:35px;top:53px;font-size:18px">Report Analytics</div>
  <p class="abs copy" style="left:35px;top:81px;width:200px;color:#444">Lorem ipsum dolor amet consectetur adipisc eiusmod incididunt labore dolore magna ullamco aliqua. Aliquip commodo consequat.</p>
  <svg class="chart" width="525" height="295" font-size="4.5" fill="#555">
    <text x="365" y="36" font-size="7" fill="#444">Chart Title</text>
    <g stroke="#e3e3e3" stroke-width=".5"><line x1="300" y1="43" x2="475" y2="43"/><line x1="300" y1="61" x2="475" y2="61"/><line x1="300" y1="79" x2="475" y2="79"/><line x1="300" y1="97" x2="475" y2="97"/><line x1="300" y1="115" x2="475" y2="115"/></g>
    <line x1="300" y1="124" x2="475" y2="124" stroke="#aaa" stroke-width=".5"/>
    <text x="293" y="45">6</text><text x="293" y="81">4</text><text x="293" y="117">2</text><text x="293" y="126">0</text>
    <g fill="none" stroke-width="1.3">
      <path d="M315 86C330 99 345 102 360 97S395 86 410 85 445 75 460 71" stroke="var(--navy)"/>
      <path d="M315 101C330 92 345 82 360 83S395 104 410 106 445 97 460 99" stroke="var(--gold)"/>
      <path d="M315 88C330 95 350 97 360 99S395 97 410 90 445 80 460 74" stroke="var(--sky)"/>
    </g>
    <text x="306" y="133">Category 1</text><text x="354" y="133">Category 2</text><text x="402" y="133">Category 3</text><text x="450" y="133">Category 4</text>
    <text x="330" y="143">— Series 1   — Series 2   — Series 3</text>

    <text x="175" y="154" font-size="7" fill="#444">Chart Title</text>
    <g stroke="#e6e6e6" stroke-width=".5"><line x1="48" y1="170" x2="350" y2="170"/><line x1="48" y1="188" x2="350" y2="188"/><line x1="48" y1="207" x2="350" y2="207"/><line x1="48" y1="225" x2="350" y2="225"/></g>
    <line x1="48" y1="244" x2="350" y2="244" stroke="#aaa" stroke-width=".5"/>
    <text x="40" y="172">6</text><text x="40" y="209">2</text><text x="40" y="246">0</text>
    <g fill="var(--navy)"><rect x="63" y="204.5" width="15" height="39.5"/><rect x="138" y="221" width="15" height="23"/><rect x="212" y="211.8" width="15" height="32.2"/><rect x="287" y="202.6" width="15" height="41.4"/></g>
    <g fill="var(--gold)"><rect x="80" y="222" width="15" height="22"/><rect x="155" y="203.5" width="15" height="40.5"/><rect x="229" y="227.4" width="15" height="16.6"/><rect x="304" y="218.2" width="15" height="25.8"/></g>
    <g fill="var(--sky)"><rect x="97" y="225.6" width="15" height="18.4"/><rect x="172" y="225.6" width="15" height="18.4"/><rect x="246" y="216.4" width="15" height="27.6"/><rect x="321" y="198" width="15" height="46"/></g>
    <g fill="#444"><text x="66" y="202">4.3</text><text x="84" y="219">2.4</text><text x="102" y="223">2</text><text x="141" y="218">2.5</text><text x="158" y="201">4.4</text><text x="177" y="223">2</text><text x="215" y="209">3.5</text><text x="232" y="225">1.8</text><text x="251" y="214">3</text><text x="290" y="200">4.5</text><text x="307" y="216">2.8</text><text x="326" y="195">5</text></g>
    <text x="78" y="253">Category 1</text><text x="152" y="253">Category 2</text><text x="226" y="253">Category 3</text><text x="301" y="253">Category 4</text>
    <text x="160" y="262">■ Series 1   ■ Series 2   ■ Series 3</text>

    <text x="415" y="163" font-size="6" fill="#444">Sales</text>
    <ellipse cx="425" cy="208" rx="46" ry="18" fill="#12355a"/>
    <path d="M425 198 L425 180 A46 18 0 0 1 468 193 Z" fill="var(--gold)"/>
    <path d="M425 198 L468 193 A46 18 0 0 1 442 214 Z" fill="var(--sky)"/>
    <path d="M425 198 L442 214 A46 18 0 0 1 379 198 A46 18 0 0 1 425 180 Z" fill="var(--navy)"/>
    <text x="388" y="253">■ 1st Qtr   ■ 2nd Qtr   ■ 3rd Qtr</text>
  </svg>
  <div class="footer-brand"><i></i>Volta Insight</div><div class="footer-rule"></div><div class="page-no">7</div>
</section>

<!-- 9 Monthly chart -->
<section class="slide" style="left:694.5px;top:418.9px">
  <div class="abs eyebrow" style="left:32px;top:38px;font-size:14px">Our Company</div>
  <div class="abs heading" style="left:32px;top:54px;font-size:21px">Monthly Chart</div>
  <svg class="chart" width="525" height="295" font-size="4.5" fill="#555">
    <circle cx="65" cy="122" r="13" fill="var(--navy)"/><circle cx="65" cy="169" r="13" fill="var(--gold)"/><circle cx="65" cy="216" r="13" fill="var(--sky)"/>
    <g fill="#fff" font-size="10" font-weight="600" text-anchor="middle"><text x="65" y="126">1</text><text x="65" y="173">2</text><text x="65" y="220">3</text></g>
    <g stroke="#ececec" stroke-width=".5"><line x1="272" y1="58" x2="500" y2="58"/><line x1="272" y1="82" x2="500" y2="82"/><line x1="272" y1="107" x2="500" y2="107"/><line x1="272" y1="131" x2="500" y2="131"/><line x1="272" y1="156" x2="500" y2="156"/><line x1="272" y1="180" x2="500" y2="180"/><line x1="272" y1="205" x2="500" y2="205"/></g>
    <line x1="272" y1="229" x2="500" y2="229" stroke="#aaa" stroke-width=".5"/>
    <g><text x="263" y="60">7</text><text x="263" y="84">6</text><text x="263" y="109">5</text><text x="263" y="133">4</text><text x="263" y="158">3</text><text x="263" y="182">2</text><text x="263" y="207">1</text><text x="263" y="231">0</text></g>
    <g fill="var(--navy)"><rect x="286" y="92" width="13" height="137"/><rect x="356" y="92" width="13" height="137"/><rect x="426" y="85" width="13" height="144"/></g>
    <g fill="var(--gold)"><rect x="300" y="114" width="13" height="115"/><rect x="370" y="68" width="13" height="161"/><rect x="440" y="146" width="13" height="83"/></g>
    <g fill="var(--sky)"><rect x="314" y="146" width="13" height="83"/><rect x="384" y="126" width="13" height="103"/><rect x="454" y="126" width="13" height="103"/></g>
    <text x="294" y="240">Category 1</text><text x="364" y="240">Category 1</text><text x="434" y="240">Category 1</text>
    <text x="345" y="251" font-size="4">■ Series 1   ■ Series 1   ■ Series 1</text>
  </svg>
  <div class="abs" style="left:93px;top:107px;font-size:8px;font-weight:600;color:var(--navy)">Lorem ipsum dolor.</div>
  <p class="abs copy" style="left:93px;top:118px;width:150px;color:#444">Lorem ipsumectetuer adipiscing elit, sed diam nonummy nibh euismod tincidunt</p>
  <div class="abs" style="left:93px;top:154px;font-size:8px;font-weight:600;color:var(--navy)">Lorem ipsum dolor.</div>
  <p class="abs copy" style="left:93px;top:165px;width:150px;color:#444">Lorem ipsumectetuer adipiscing elit, sed diam nonummy nibh euismod tincidunt</p>
  <div class="abs" style="left:93px;top:201px;font-size:8px;font-weight:600;color:var(--navy)">Lorem ipsum dolor.</div>
  <p class="abs copy" style="left:93px;top:212px;width:150px;color:#444">Lorem ipsumectetuer adipiscing elit, sed diam nonummy nibh euismod tincidunt</p>
  <div class="footer-brand"><i></i>Volta Insight</div><div class="footer-rule"></div><div class="page-no">8</div>
</section>

<!-- 10 Platform overview -->
<section class="slide" style="left:48px;top:605.7px">
  <div class="abs eyebrow" style="left:32px;top:43px;font-size:14px">Our Company</div>
  <div class="abs heading" style="left:32px;top:59px;font-size:19px">Platform Overview</div>
  <div class="abs" style="left:32px;top:118px;font-size:8px;font-weight:600;color:var(--ink)">Project Problem</div>
  <p class="abs copy" style="left:32px;top:130px;width:118px;font-size:5.4px">Lorem ipsum dolor sit amet, cons ectetuer adipiscing elit, sed diam nonummy nibh euismod tincidunt.Lorem ipsum dolor sit amet.</p>
  <div class="abs" style="left:162px;top:118px;font-size:8px;font-weight:600;color:var(--ink)">Project Solution</div>
  <p class="abs copy" style="left:162px;top:130px;width:118px;font-size:5.4px">Lorem ipsum dolor sit amet, cons ectetuer adipiscing elit, sed diam nonummy nibh euismod tincidunt.Lorem ipsum dolor sit amet.</p>
  <div class="abs" style="left:32px;top:178px;font-size:8px;font-weight:600;color:var(--ink)">Project Problem</div>
  <p class="abs copy" style="left:32px;top:190px;width:118px;font-size:5.4px">Lorem ipsum dolor sit amet, cons ectetuer adipiscing elit, sed diam nonummy nibh euismod tincidunt.Lorem ipsum dolor sit amet.</p>
  <div class="abs" style="left:162px;top:178px;font-size:8px;font-weight:600;color:var(--ink)">Project Solution</div>
  <p class="abs copy" style="left:162px;top:190px;width:118px;font-size:5.4px">Lorem ipsum dolor sit amet, cons ectetuer adipiscing elit, sed diam nonummy nibh euismod tincidunt.Lorem ipsum dolor sit amet.</p>
  <div class="tile" style="left:310px;top:82px;background:var(--navy);border-radius:8px 0 0 0">
    <svg width="12" height="12" fill="none" stroke="#fff" stroke-width="1"><circle cx="6" cy="5" r="4"/><path d="M4 10h4"/></svg>
    <h4>PROBLEM</h4><p>Lorem ipsum dolor sit amet, cons ectetuer adipiscing elit, sed diam nonummy.</p></div>
  <div class="tile" style="left:399px;top:82px;background:var(--gold);border-radius:0 8px 0 0">
    <svg width="12" height="12" fill="none" stroke="#fff" stroke-width="1"><circle cx="6" cy="6" r="3"/><path d="M6 0v2M6 10v2M0 6h2M10 6h2"/></svg>
    <h4>SOLUTION</h4><p>Lorem ipsum dolor sit amet, cons ectetuer adipiscing elit, sed diam nonummy.</p></div>
  <div class="tile" style="left:310px;top:168px;background:var(--gold);border-radius:0 0 0 8px">
    <svg width="12" height="12" fill="none" stroke="#fff" stroke-width="1"><path d="M1 11h10M3 10V6M6 10V3M9 10V5"/></svg>
    <h4>MARKET</h4><p>Lorem ipsum dolor sit amet, cons ectetuer adipiscing elit, sed diam nonummy.</p></div>
  <div class="tile" style="left:399px;top:168px;background:var(--navy);border-radius:0 0 8px 0">
    <svg width="12" height="12" fill="none" stroke="#fff" stroke-width="1"><circle cx="6" cy="6" r="5"/><circle cx="6" cy="6" r="2"/></svg>
    <h4>MISSION</h4><p>Lorem ipsum dolor sit amet, cons ectetuer adipiscing elit, sed diam nonummy.</p></div>
  <div class="footer-brand"><i></i>Volta Insight</div><div class="footer-rule"></div><div class="page-no">9</div>
</section>

<!-- 11 Market analysis -->
<section class="slide" style="left:372.6px;top:605.7px">
  <div class="abs eyebrow" style="left:22px;top:20px;font-size:13px">Market Analysis</div>
  <div class="abs heading" style="left:22px;top:35px;font-size:18px">For A Business Plan</div>
  <svg class="chart" width="525" height="295">
    <g stroke="#fff" stroke-width="3">
      <path d="M264 86A72 72 0 0 0 192 158H224A40 40 0 0 1 264 118Z" fill="var(--navy)"/>
      <path d="M264 86A72 72 0 0 1 336 158H304A40 40 0 0 0 264 118Z" fill="var(--gold)"/>
      <path d="M336 158A72 72 0 0 1 264 230V198A40 40 0 0 0 304 158Z" fill="var(--navy)"/>
      <path d="M264 230A72 72 0 0 1 192 158H224A40 40 0 0 0 264 198Z" fill="var(--gold)"/>
    </g>
    <g fill="none" stroke="#fff" stroke-width="1.2">
      <circle cx="226" cy="120" r="7"/><circle cx="226" cy="120" r="3"/>
      <path d="M296 124l10-10M300 114h6v6"/>
      <circle cx="302" cy="196" r="7"/><path d="M302 189v14"/>
      <rect x="219" y="190" width="13" height="10" rx="2"/>
    </g>
  </svg>
  <div class="abs" style="left:224px;top:143px;width:80px;text-align:center;font-size:12px;font-weight:700;color:var(--ink);line-height:1.1">Text<br>Added</div>
  <div class="abs" style="left:60px;top:83px;width:113px;text-align:right"><div style="font-size:10px;font-weight:600;color:var(--ink)">Text Here</div><p class="copy" style="font-size:5.3px">Lorem ipsum dolor sit amet, consectetuer adipiscing elit, sed diammy nibh euismod tincidunt ut laoreet dolore</p></div>
  <div class="abs" style="left:350px;top:83px;width:120px"><div style="font-size:10px;font-weight:600;color:var(--ink)">Text Here</div><p class="copy" style="font-size:5.3px">Lorem ipsum dolor sit amet, consectetuer adipiscing elit, sed diammy nibh euismod tincidunt ut laoreet dolore</p></div>
  <div class="abs" style="left:60px;top:190px;width:113px;text-align:right"><div style="font-size:10px;font-weight:600;color:var(--ink)">Text Here</div><p class="copy" style="font-size:5.3px">Lorem ipsum dolor sit amet, consectetuer adipiscing elit, sed diammy nibh euismod tincidunt ut laoreet dolore</p></div>
  <div class="abs" style="left:350px;top:190px;width:120px"><div style="font-size:10px;font-weight:600;color:var(--ink)">Text Here</div><p class="copy" style="font-size:5.3px">Lorem ipsum dolor sit amet, consectetuer adipiscing elit, sed diammy nibh euismod tincidunt ut laoreet dolore</p></div>
  <div class="footer-brand"><i></i>Volta Insight</div><div class="footer-rule"></div><div class="page-no">10</div>
</section>

<!-- 12 Table -->
<section class="slide" style="left:694.5px;top:605.7px">
  <div class="abs eyebrow" style="left:26px;top:26px;font-size:15px">Text</div>
  <div class="abs heading" style="left:26px;top:42px;font-size:19px">Added Hare</div>
  <p class="abs copy" style="left:26px;top:70px;width:140px;font-size:6px">Lorem ipsum dolor sit amet, consectetuer ex ea commodo consequat.</p>
  <p class="abs copy" style="left:26px;top:100px;width:140px;font-size:6px">Duis autem vel eum iriure dolor in invulputate velit esse molestie consequat, vel illum dolore eu feugiat nulla facilisis at vero eros et accumsan et iusto odio dignissim qui blandit praesent luptatum zzril delenit augue duis dolore</p>
  <p class="abs copy" style="left:26px;top:190px;width:140px;font-size:6px">Lorem ipsum dolor sit amet, cons ectetueradipiscing elit, sed diam nonummy nibh euismod tincidunt ut laoreet dolore.</p>
  <table class="data-table">
    <tr><th>Text Added Here</th><th>Text One</th><th>Text Two</th><th>Text Three</th></tr>
    <tr><td>Title Text one</td><td></td><td></td><td></td></tr>
    <tr><td>Title Text Two</td><td></td><td></td><td></td></tr>
    <tr><td>Title Text Three</td><td></td><td></td><td></td></tr>
    <tr><td>Title Text Four</td><td></td><td></td><td></td></tr>
    <tr><td>Title Text Five</td><td></td><td></td><td></td></tr>
  </table>
  <div class="footer-brand"><i></i>Volta Insight</div><div class="footer-rule"></div><div class="page-no">13</div>
</section>

<!-- 13 Content summary -->
<section class="slide" style="left:48px;top:794.6px">
  <div class="abs eyebrow" style="left:16px;top:18px;font-size:15px">Report</div>
  <div class="abs heading" style="left:16px;top:34px;font-size:19px">Content Summary</div>
  <div class="abs" style="left:34px;top:77px;width:210px">
    <div style="font-size:9px;font-weight:600;color:var(--navy)">01. Aliquam Erat Volutpat</div>
    <p class="copy" style="font-size:5.6px;margin:3px 0 6px">Lorem ipsum dolor sit amet, consectetuer adipiscing elit, sed diamnonummy nibh euismod</p>
    <p class="copy" style="font-size:5.6px">Lorem ipsum dolor sit amet, cons ectetuer adipiscing elit, sed diamnonummy nibh euismod tincidunt ut laoreet sed diam cons ectetuer adipiscing elit</p>
    <div style="font-size:9px;font-weight:600;color:var(--navy);margin-top:13px">02. Consectetuer Adipiscing Elit</div>
    <p class="copy" style="font-size:5.6px;margin:3px 0 6px">Lorem ipsum dolor sit amet, consectetuer adipiscing elit, sed diamnonummy nibh euismod</p>
    <p class="copy" style="font-size:5.6px">Lorem ipsum dolor sit amet, cons ectetuer adipiscing elit, sed diamnonummy nibh euismod tincidunt ut laoreet sed diam cons ectetuer adipiscing elit</p>
  </div>
  <div class="abs" style="left:283px;top:77px;width:210px">
    <div style="font-size:9px;font-weight:600;color:var(--navy)">03. Aliquam Erat Volutpat</div>
    <p class="copy" style="font-size:5.6px;margin:3px 0 6px">Lorem ipsum dolor sit amet, consectetuer adipiscing elit, sed diam nonummy nibh euismod</p>
    <p class="copy" style="font-size:5.6px">Lorem ipsum dolor sit amet, cons ectetuer adipiscing elit, sed diam nonummy nibh cons ectetuer adipiscing elit</p>
    <div style="margin-top:8px;padding-left:16px;font-size:4.6px;color:var(--muted);line-height:1.4">
      <div style="font-size:5.6px;font-weight:600;color:var(--navy)">Lorem ipsum dolor</div><p>Lorem ipsum dolor sit amet, consectetuer adipiscing elit, sed diam nonummy nibh euismod tincidunt ut laoreet</p>
      <div style="font-size:5.6px;font-weight:600;color:var(--navy);margin-top:5px">Lorem ipsum dolor</div><p>Lorem ipsum dolor sit amet, consectetuer adipiscing elit sed diam nonummy nibh euismod tincidunt ut laoreet</p>
      <div style="font-size:5.6px;font-weight:600;color:var(--navy);margin-top:5px">Lorem ipsum dolor</div><p>Lorem ipsum dolor sit amet, consectetuer adipiscing elit, sed diam nonummy nibh euismod tincidunt ut laoreet</p>
    </div>
  </div>
  <div class="footer-brand"><i></i>Volta Insight</div><div class="footer-rule"></div><div class="page-no">11</div>
</section>

<!-- 14 Clients -->
<section class="slide" style="left:372.6px;top:794.6px">
  <div class="abs heading" style="left:20px;top:24px;font-size:18px"><span style="color:var(--gold)">Our</span> Clients</div>
  <p class="abs copy" style="left:20px;top:50px;width:250px;font-size:5.8px">Lorem ipsum dolor sit amet, consectetuer adipiscing elit, sed diam nonummy nibh euismod tincidunt ut laoreet dolore magna aliquam erat volutpat.</p>
  <p class="abs copy" style="left:20px;top:74px;width:250px;font-size:5.8px">Ut wisi enim ad minim veniam, quis nostrud exerci tation ullamcorper suscipit lobortis nisl ut aliquip ex ea commodo consequat.</p>
  <div class="check" style="left:33px;top:130px"><i></i>Make Simple Text</div>
  <p class="abs copy" style="left:53px;top:148px;width:200px;font-size:5.4px;color:#444">Nemo enim ipsam voluptatem quia voluptas aspernat fugit sed quia magni dolore ratione is voluptas neque porro quisquam sequi nesciunt.</p>
  <div class="check" style="left:33px;top:188px"><i></i>Make Simple Text</div>
  <p class="abs copy" style="left:53px;top:206px;width:200px;font-size:5.4px;color:#444">Nemo enim ipsam voluptatem quia voluptas aspernat fugit sed quia magni dolore ratione voluptas.</p>
  <div class="client" style="left:293px;top:40px">Brightline Guild</div>
  <div class="client" style="left:390px;top:40px">Korvane</div>
  <div class="client" style="left:293px;top:96px">Delmora</div>
  <div class="client" style="left:390px;top:96px">Sunpath</div>
  <div class="client" style="left:293px;top:152px">Ravelle Grid</div>
  <div class="client" style="left:390px;top:152px">Northway</div>
  <div class="client" style="left:293px;top:208px">Tamsen</div>
  <div class="client" style="left:390px;top:208px">Quellfeld</div>
  <div class="footer-brand"><i></i>Volta Insight</div><div class="footer-rule"></div><div class="page-no">13</div>
</section>

<!-- 15 Timeline -->
<section class="slide" style="left:694.5px;top:794.6px">
  <div class="abs eyebrow" style="left:30px;top:26px;font-size:14px">Our Company</div>
  <div class="abs heading" style="left:30px;top:42px;font-size:19px">Timeline</div>
  <svg class="chart" width="525" height="295">
    <polygon points="66,162 146,162 138,177 56,177" fill="var(--navy)"/>
    <polygon points="146,162 226,162 218,177 138,177" fill="var(--gold)"/>
    <polygon points="226,162 306,162 298,177 218,177" fill="var(--navy)"/>
    <polygon points="306,162 386,162 378,177 298,177" fill="var(--gold)"/>
    <polygon points="386,162 466,162 474,177 378,177" fill="var(--navy)"/>
    <g font-size="6" font-weight="600" fill="#fff" text-anchor="middle"><text x="101" y="172">1990</text><text x="183" y="172">2001</text><text x="262" y="172">2007</text><text x="343" y="172">2012</text><text x="426" y="172">2020</text></g>
    <g stroke="var(--navy)" stroke-width="1.5"><line x1="101" y1="136" x2="101" y2="156"/><line x1="262" y1="136" x2="262" y2="156"/><line x1="426" y1="136" x2="426" y2="156"/></g>
    <g fill="var(--navy)"><circle cx="101" cy="136" r="2.5"/><circle cx="262" cy="136" r="2.5"/><circle cx="426" cy="136" r="2.5"/></g>
    <g stroke="var(--gold)" stroke-width="1.5"><line x1="183" y1="183" x2="183" y2="201"/><line x1="343" y1="183" x2="343" y2="201"/></g>
    <g fill="var(--gold)"><circle cx="183" cy="201" r="2.5"/><circle cx="343" cy="201" r="2.5"/></g>
  </svg>
  <div class="abs" style="left:61px;top:98px;width:80px;text-align:center"><div style="font-size:8px;font-weight:600;color:var(--navy)">Your Title</div><p class="copy" style="font-size:5.4px;line-height:1.3">Refers to a good or service being offered</p></div>
  <div class="abs" style="left:222px;top:98px;width:80px;text-align:center"><div style="font-size:8px;font-weight:600;color:var(--navy)">Your Title</div><p class="copy" style="font-size:5.4px;line-height:1.3">Refers to a good or service being offered</p></div>
  <div class="abs" style="left:386px;top:98px;width:80px;text-align:center"><div style="font-size:8px;font-weight:600;color:var(--navy)">Your Title</div><p class="copy" style="font-size:5.4px;line-height:1.3">Refers to a good or service being offered</p></div>
  <div class="abs" style="left:143px;top:207px;width:80px;text-align:center"><div style="font-size:8px;font-weight:600;color:var(--gold)">Your Title</div><p class="copy" style="font-size:5.4px;line-height:1.3">Refers to a good or service being offered</p></div>
  <div class="abs" style="left:303px;top:207px;width:80px;text-align:center"><div style="font-size:8px;font-weight:600;color:var(--gold)">Your Title</div><p class="copy" style="font-size:5.4px;line-height:1.3">Refers to a good or service being offered</p></div>
  <div class="footer-brand"><i></i>Volta Insight</div><div class="footer-rule"></div><div class="page-no">13</div>
</section>

<!-- 16 Growth -->
<section class="slide" style="left:48px;top:980.6px">
  <svg class="chart" width="525" height="295"><path d="M245 0H525V260H245V80Q268 70 262 40Q255 20 245 0Z" fill="var(--navy)"/></svg>
  <div class="abs eyebrow" style="left:27px;top:22px;font-size:13px">The Truth</div>
  <div class="abs heading" style="left:27px;top:37px;font-size:19px">About Company<br>Growth</div>
  <p class="abs copy" style="left:27px;top:88px;width:200px;color:#444;font-size:7px">Lorem ipsum dolor sit amet consect adipisc elit incididunt labore dolore aliqua.</p>
  <div class="check" style="left:58px;top:135px"><i></i>Make Simple Text</div>
  <p class="abs copy" style="left:58px;top:153px;width:180px;font-size:5.2px;color:#444">Nemo enim ipsam voluptatem quia voluptas aspernat fugit sed quia magni dolore ratione is voluptas neque porro quisquam sequi nesciunt.</p>
  <div class="check" style="left:58px;top:198px"><i></i>Make Simple Text</div>
  <p class="abs copy" style="left:58px;top:216px;width:180px;font-size:5.2px;color:#444">Nemo enim ipsam voluptatem quia voluptas aspernat fugit sed quia magni dolore ratione voluptas.</p>
  <div class="photo" role="img" aria-label="Team reviewing documents at a desk" style="left:285px;top:33px;width:208px;height:182px;background:linear-gradient(150deg,#e9ecef 0%,#c5ccd4 50%,#8d96a0 100%)"></div>
  <div class="abs" style="left:268px;top:215px;width:38px;height:45px;background:var(--gold)"></div>
  <svg class="chart" width="525" height="295" fill="none" stroke="#fff" stroke-width="1.4"><path d="M281 229h12v5a6 6 0 0 1-12 0zM281 231h-3a3 3 0 0 0 3 4M293 231h3a3 3 0 0 1-3 4M287 240v4M283 246h8"/></svg>
  <div class="abs" style="left:320px;top:224px;font-size:19px;font-weight:700;color:#fff">100K</div>
  <div class="abs" style="left:382px;top:222px;width:1px;height:32px;background:#fff"></div>
  <div class="abs" style="left:400px;top:224px;font-size:19px;font-weight:700;color:#fff">+1M</div>
  <div class="footer-brand"><i></i>Volta Insight</div><div class="footer-rule"></div><div class="page-no">12</div>
</section>

<!-- 17 Text with screen -->
<section class="slide" style="left:372.6px;top:980.6px">
  <div class="abs eyebrow" style="left:27px;top:18px;font-size:14px">Text</div>
  <div class="abs heading" style="left:27px;top:34px;font-size:19px">Added Hare</div>
  <div class="abs" style="left:27px;top:70px;width:170px">
    <p class="copy" style="font-size:5.6px;color:#444">Lorem ipsum dolor sit amet consectetuer adipiscing elit, sed diam nonummy nibh euismod tincidunt ut laoreet dolore magna aliquam erat volutpat.Ut wisi enim ad minim veniam</p>
    <p class="copy" style="font-size:5.6px;color:#444;margin-top:7px">quis nostrud exerci tation ullamcorper suscipit lobortis nisl ut aliquip ex ea commodo consequat. Lorem ipsum dolor sit amet consectetuer adipiscing elit, sed diam nonummy nibh euismod tincidunt ut laoreet dolore magna aliquam erat volutpat.</p>
    <p class="copy" style="font-size:5.6px;color:#444;margin-top:7px">Ut wisi enim ad minim veniam quis nostrud exerci tation ullamcorper suscipit lobortis nisl ut aliquip ex ea commodo consequat.</p>
  </div>
  <div class="photo" role="img" aria-label="Laptop showing a team meeting around a table" style="left:240px;top:80px;width:257px;height:155px;border-radius:6px;background:linear-gradient(160deg,#c9ced4 0%,#7d8ea0 45%,#3b4656 100%)"></div>
  <div class="footer-brand"><i></i>Volta Insight</div><div class="footer-rule"></div><div class="page-no">13</div>
</section>

<!-- 18 Contact -->
<section class="slide" style="left:694.5px;top:980.6px">
  <div class="abs heading" style="left:0;top:48px;width:525px;text-align:center;font-size:22px">Contact <span style="color:var(--gold)">Us</span></div>
  <p class="abs copy" style="left:100px;top:80px;width:325px;text-align:center;font-size:6px">laoreet dolore magna aliquam erat volutpat. Ut wisi enim ad minim veniam, quis nostrud exerci aliquam erat volutpat. Ut wisi enim.</p>
  <div class="abs" style="left:38px;top:127px;width:449px;height:83px;background:var(--navy);border-radius:16px"></div>
  <svg class="chart" width="525" height="295">
    <g fill="var(--gold)"><circle cx="64" cy="168" r="6"/><circle cx="206" cy="168" r="6"/><circle cx="342" cy="168" r="6"/></g>
    <g fill="none" stroke="var(--navy)" stroke-width="1.2"><path d="M64 172c-2-3-3-4-3-6a3 3 0 0 1 6 0c0 2-1 3-3 6z"/><path d="M203 165c1 3 3 5 6 6l1-2-2-1-1 1-2-2 1-1-1-2z"/><rect x="339" y="166" width="6" height="4"/><path d="M339 166l3 2 3-2"/></g>
  </svg>
  <div class="abs" style="left:75px;top:160px;font-size:6.4px;color:#fff;line-height:1.35">Address Street Name<br>City Name, Country 000</div>
  <div class="abs" style="left:218px;top:160px;font-size:6.4px;color:#fff;line-height:1.35">(+000) 123 456 789<br>(+000) 123 456 789</div>
  <div class="abs" style="left:354px;top:160px;font-size:6.4px;color:#fff;line-height:1.35">Info@example.com<br>Www.example.com</div>
  <div class="abs" style="left:0;top:230px;width:525px;text-align:center;font-size:8px;letter-spacing:4px;color:var(--ink)">www.<span style="color:var(--gold)">website</span>.com</div>
</section>

</main>
</body>
</html>
```